Business Card Design

We need a business card design for a new dental practice in Brisbane. I'd like the basic details and logo on one side and appointment schedule on the other side. It is based in CBD office area and would prefer a professional and modern design.
Target Market(s)
20-60 years old office workers and residents with high education levels
Industry/Entity Type
Dental
Contact Information for Business Card
Harbourlight Dental
Dr Glenn Marwick
Principal Dentist
07 3964 2275
admin@harbourlightsmiles.com.au
www.harbourlightsmiles.com.au
S27, Level 3, Ardent North Plaza, 814 Tallowood Rd, Kelsey Heights, QLD 4019

```html
<!DOCTYPE html>
<html lang="en">
<head>
<meta charset="utf-8">
<title>Harbourlight Dental – Business Card</title>
<link rel="stylesheet" href="https://fonts.googleapis.com/css2?family=Open+Sans:wght@400;600;700&display=swap">
<style>
  :root {
    --backdrop: #d4d5d7;
    --card: #ffffff;
    --ink-dark: #1b2433;
    --ink-grey: #7a7c80;
    --brand-blue: #4eb1e3;
    --brand-blue-text: #2fa3dc;
    --mark-blue: #3f95cc;
    --white: #ffffff;
  }
  * { margin: 0; padding: 0; box-sizing: border-box; }
  html, body { width: 1200px; height: 1200px; overflow: hidden; }
  body {
    background: var(--backdrop);
    font-family: "Open Sans", Arial, sans-serif;
    position: relative;
  }
  .card {
    position: absolute;
    left: 216px;
    width: 764px;
    height: 462px;
    background: var(--card);
    overflow: hidden;
    box-shadow: 0 2px 6px rgba(0,0,0,0.12);
  }
  .card--front { top: 130px; height: 460px; }
  .card--back { top: 600px; }

  .practitioner { position: absolute; left: 482px; top: 52px; }
  .practitioner__name { font-size: 26px; font-weight: 700; color: var(--ink-dark); line-height: 1.2; }
  .practitioner__role { font-size: 19px; color: var(--brand-blue-text); line-height: 1.3; }

  .brand-dot { position: absolute; border-radius: 50%; background: var(--mark-blue); }
  .brand-name { position: absolute; font-weight: 400; color: var(--ink-dark); white-space: nowrap; letter-spacing: -0.3px; }
  .card--front .brand-dot { left: 140px; top: 122px; width: 104px; height: 104px; }
  .card--front .brand-name { left: 34px; top: 226px; font-size: 36px; }

  .contact { position: absolute; left: 388px; font-size: 20px; color: var(--ink-grey); line-height: 26px; }
  .contact__row { display: flex; gap: 10px; }
  .contact__icon { width: 14px; height: 26px; flex: none; display: flex; align-items: center; }
  .contact--address { top: 258px; }
  .contact--phone { top: 350px; }
  .contact--email { top: 378px; }

  .web-band {
    position: absolute; left: 336px; top: 408px; width: 428px; height: 52px;
    background: var(--brand-blue);
    border-top-left-radius: 56px 52px;
    display: flex; align-items: center; padding-left: 52px; gap: 10px;
    color: var(--white); font-size: 20px;
  }

  .appointment { position: absolute; left: 32px; top: 58px; color: var(--ink-grey); }
  .appointment__title { font-size: 21px; line-height: 1.4; }
  .appointment__line { font-size: 18px; line-height: 28px; margin-left: 32px; }
  .tick-box { display: inline-block; width: 15px; height: 15px; border: 1.5px solid var(--ink-grey); vertical-align: -1px; margin-right: 4px; }
  .blank { display: inline-block; border-bottom: 1.5px solid var(--ink-grey); height: 18px; vertical-align: -2px; }

  .back-band { position: absolute; left: 0; top: 263px; width: 764px; height: 199px; background: var(--brand-blue); }
  .back-band .brand-dot { left: 569px; top: 37px; width: 76px; height: 76px; }
  .back-band .brand-name { right: 32px; top: 112px; font-size: 31px; }
  .back-band__web { position: absolute; right: 32px; top: 154px; font-size: 20px; color: var(--white); }
</style>
</head>
<body>
  <section class="card card--front">
    <div class="practitioner">
      <div class="practitioner__name">Dr Glenn Marwick</div>
      <div class="practitioner__role">Principal Dentist</div>
    </div>

    <div class="brand-dot"></div>
    <div class="brand-name">Harbourlight Dental</div>

    <div class="contact contact--address">
      <div class="contact__row">
        <span class="contact__icon"><svg width="14" height="12" viewBox="0 0 14 12"><path d="M7 0 L14 6 H12 V12 H8.5 V8 H5.5 V12 H2 V6 H0 Z" fill="var(--brand-blue)"/></svg></span>
        <span>S27, Level 3, Ardent North Plaza<br>814 Tallowood Rd, Kelsey Heights<br>QLD 4019</span>
      </div>
    </div>
    <div class="contact contact--phone">
      <div class="contact__row">
        <span class="contact__icon"><svg width="10" height="16" viewBox="0 0 10 16"><rect x="1" y="0" width="8" height="16" rx="1.5" fill="var(--brand-blue)"/><rect x="2.5" y="2" width="5" height="7" fill="#fff"/></svg></span>
        <span>07 3964 2275</span>
      </div>
    </div>
    <div class="contact contact--email">
      <div class="contact__row">
        <span class="contact__icon"><svg width="15" height="11" viewBox="0 0 15 11"><rect width="15" height="11" rx="1" fill="var(--brand-blue)"/><path d="M0.5 1 L7.5 6.5 L14.5 1" stroke="#fff" stroke-width="1.4" fill="none"/></svg></span>
        <span>admin@harbourlightsmiles.com.au</span>
      </div>
    </div>

    <div class="web-band">
      <svg width="18" height="18" viewBox="0 0 18 18" fill="none" stroke="#fff" stroke-width="1.3"><circle cx="9" cy="9" r="8"/><ellipse cx="9" cy="9" rx="3.5" ry="8"/><path d="M1 9 H17 M2.5 5 H15.5 M2.5 13 H15.5"/></svg>
      <span>www.harbourlightsmiles.com.au</span>
    </div>
  </section>

  <section class="card card--back">
    <div class="appointment">
      <div class="appointment__title">Next Appointment:</div>
      <div class="appointment__line">Mon<span class="tick-box"></span> Tue<span class="tick-box"></span> Wed<span class="tick-box"></span> Thur<span class="tick-box"></span></div>
      <div class="appointment__line">Date:<span class="blank" style="width:84px"></span>at<span class="blank" style="width:48px"></span>AM<span class="tick-box"></span> PM<span class="tick-box"></span></div>
    </div>

    <div class="back-band">
      <div class="brand-dot"></div>
      <div class="brand-name">Harbourlight Dental</div>
      <div class="back-band__web">www.harbourlightsmiles.com.au</div>
    </div>
  </section>
</body>
</html>
```